Design for Torvel Ginger Chewy Candy!

Hello! We are Torvel Enterprises Corp, a food manufacturer and distributor based in Los Angeles, CA. We manufacture Chips, Cookies, Juices, Dairy, and last but not least, Candies! We are launching our Ginger Chewy Candy soon and we need a great design for it!

Our Ginger Chewy Candy is a perfect mixture between sweet and spicy from the ginger itself. Torvel Ginger Chewy Candy a good relief for sore throat and nausea.

Now, other than a great design, we also welcome brand suggestions for the candy.
If you can come up with a logo for the Ginger Candy, that would be swell!

We are open to unique and out of the box design. We chose a few color schemes for the design, but feel free to step out of the box if you feel it suits the brand.

We don't have the exact size for the plastic pouch, but it should be a generic small plastic pouch size (approximately 4 oz resealable plastic pouch)

Please have fun designing the project, we can't wait to see all the great designs!

Cheers!

Target Market(s)

USA and Asian market
Age 30-70
Male and Female

Industry/Entity Type

Manufacture

Font styles to use
Serif
Sans Serif
Decorative

Colors
fff3d1
fee18a
fece3e
fbc994
fce8d3

Requirements
Must have
• Torvel Logo
• A picture of ginger (illustrations or photographs are welcome)
Nice to have
• Coating suggestions like Matte surface or SPOT UV
• Give us ideas of what the name of the chewy candy should be. Product name ideas are welcome!

```html
<!DOCTYPE html>
<html lang="en">
<head>
<meta charset="utf-8">
<title>Ginvel Ginger Chewy Candy – Pouch Design</title>
<link rel="stylesheet" href="https://fonts.googleapis.com/css2?family=Baloo+2:wght@600;800&family=Oswald:wght@500&display=swap">
<style>
  :root {
    --backdrop: #f4f4f6;
    --navy: #1d2f7c;
    --blue: #1a8fd6;
    --leaf-green: #8aac1f;
    --leaf-green-dark: #6f8f14;
    --sun-yellow: #e6d21c;
    --sun-yellow-deep: #cbb913;
    --ginger-light: #e0c49a;
    --ginger-dark: #b38d5c;
    --white: #ffffff;
  }
  html, body {
    margin: 0;
    padding: 0;
    width: 1124px;
    height: 1200px;
    overflow: hidden;
    background: var(--backdrop);
  }
  .canvas {
    position: relative;
    width: 1124px;
    height: 1200px;
  }
  .pouch {
    position: absolute;
    left: 312px;
    top: 40px;
    width: 500px;
    height: 720px;
    filter: drop-shadow(0 10px 18px rgba(0,0,0,0.12));
  }
  .net-weight {
    font-family: "Baloo 2", sans-serif;
    font-weight: 800;
    font-size: 17px;
    fill: var(--navy);
  }
  .brand-name {
    font-family: "Baloo 2", sans-serif;
    font-weight: 800;
    font-size: 36px;
    fill: var(--navy);
  }
  .product-name {
    font-family: "Baloo 2", sans-serif;
    font-weight: 800;
    font-size: 84px;
    fill: var(--navy);
  }
  .product-label {
    font-family: "Oswald", sans-serif;
    font-weight: 500;
    font-size: 24px;
    fill: var(--white);
    letter-spacing: 0.5px;
  }
  .tagline-small {
    font-family: "Baloo 2", sans-serif;
    font-weight: 600;
    font-size: 18px;
    fill: var(--navy);
  }
  .tagline-large {
    font-family: "Baloo 2", sans-serif;
    font-weight: 800;
    font-size: 27px;
    fill: var(--navy);
  }
  .product-wordmark {
    position: absolute;
    left: 0;
    top: 820px;
    width: 1124px;
    text-align: center;
    font-family: "Baloo 2", sans-serif;
    font-weight: 800;
    font-size: 230px;
    line-height: 1;
    color: var(--navy);
    letter-spacing: -4px;
  }
</style>
</head>
<body>
<main class="canvas">
  <svg class="pouch" viewBox="0 0 500 720" xmlns="http://www.w3.org/2000/svg">
    <defs>
      <linearGradient id="ginger-tone" x1="0" y1="0" x2="1" y2="1">
        <stop offset="0" stop-color="var(--ginger-light)"/>
        <stop offset="1" stop-color="var(--ginger-dark)"/>
      </linearGradient>
    </defs>

    <!-- pouch body -->
    <rect class="pouch-body" x="0" y="0" width="500" height="720" fill="var(--white)"/>

    <!-- top seal band -->
    <rect x="0" y="0" width="500" height="26" fill="var(--blue)"/>
    <g stroke="var(--navy)" stroke-opacity="0.25" stroke-width="1">
      <line x1="0" y1="7" x2="500" y2="7"/>
      <line x1="0" y1="13" x2="500" y2="13"/>
      <line x1="0" y1="19" x2="500" y2="19"/>
    </g>

    <!-- green header with pattern area -->
    <rect x="0" y="26" width="500" height="200" fill="var(--leaf-green)" role="img" aria-label="Green header with swirling ginger-root pattern"/>

    <!-- header wave edge -->
    <path d="M0 212 C110 178 190 186 250 198 C330 214 420 200 500 168 L500 232 L0 232 Z" fill="var(--blue)"/>
    <path d="M0 224 C110 190 190 198 250 210 C330 226 420 212 500 180 L500 560 L0 560 Z" fill="var(--white)"/>

    <!-- brand shield -->
    <path d="M150 26 L350 26 L350 120 L250 168 L150 120 Z" fill="var(--blue)"/>
    <path d="M160 26 L340 26 L340 113 L250 156 L160 113 Z" fill="var(--white)"/>
    <text class="brand-name" x="250" y="100" text-anchor="middle">Torvel</text>

    <text class="net-weight" x="36" y="86">NET WT 4 OZ</text>

    <!-- product name -->
    <text class="product-name" x="250" y="300" text-anchor="middle">GINVEL</text>

    <!-- ginger photo area -->
    <path d="M88 430 C80 370 140 330 210 338 C260 320 330 322 372 350 C420 372 432 430 410 470 C380 520 300 530 240 520 C170 526 100 500 88 430 Z"
          fill="url(#ginger-tone)" role="img" aria-label="Photograph of fresh ginger root with round golden slices"/>

    <!-- product label -->
    <rect x="108" y="446" width="284" height="46" rx="6" fill="var(--navy)"/>
    <rect x="113" y="451" width="274" height="36" rx="4" fill="none" stroke="var(--white)" stroke-opacity="0.5" stroke-dasharray="3 3"/>
    <text class="product-label" x="250" y="478" text-anchor="middle">GINGER CHEWY CANDY</text>

    <!-- bottom wave and yellow base -->
    <path d="M0 560 C90 550 160 518 250 528 C340 538 420 566 500 540 L500 720 L0 720 Z" fill="var(--blue)"/>
    <path d="M0 572 C90 562 160 532 250 542 C340 552 420 580 500 554 L500 720 L0 720 Z" fill="var(--sun-yellow)"/>

    <text class="tagline-small" x="250" y="604" text-anchor="middle">...a good relief for</text>
    <text class="tagline-large" x="250" y="636" text-anchor="middle">sore throat and nausea.</text>

    <!-- bottom seal stripes -->
    <g stroke="var(--sun-yellow-deep)" stroke-width="2">
      <line x1="0" y1="664" x2="500" y2="664"/>
      <line x1="0" y1="672" x2="500" y2="672"/>
      <line x1="0" y1="680" x2="500" y2="680"/>
      <line x1="0" y1="688" x2="500" y2="688"/>
      <line x1="0" y1="696" x2="500" y2="696"/>
      <line x1="0" y1="704" x2="500" y2="704"/>
      <line x1="0" y1="712" x2="500" y2="712"/>
    </g>
  </svg>

  <div class="product-wordmark">GINVEL</div>
</main>
</body>
</html>
```